VMGD - Velvet Marrow Glee Den - Craft Cocktails Mixes.

and we want to sell craft cocktails mixes (dried ingredients) in jars. The person buying them would add the alcohol.

LOGO TO BE WHITE ON WEBSITE

We are doing something similar to this, but would like to make them better... with better names and better mixers.

Here are some competing sites.

https://www.dunmoreshakers.com

https://pelkintonic.com

In terms of style, I love this layout and look of a website:

https://www.rvharborsotol.com/

Or this

https://www.knitthevale.com/

Target Market(s)

Target market is 21-50. Anyone who wants to throw a party or make amazing cocktails, but doesn't have the full bar to do so. It's just pour... wait 3 days. Strain. Mix with soda, tonic, fruit juice, kombucha over ice and drink.

Coding

Coded - Design and coding required

Number of Pages Required

5+ page

Other font styles liked:
• LOGO TO BE WHITE ON WEBSITE - Match the font of the Logo

Colors
00AB8E
00BBA5
67D7C9
C6EFE9
E9F9F6

Requirements
Must have
• Point of sale. The ability to add photos and videos with ease
Nice to have
• Great photography. Teal background tabs with white logo.

```html
<!DOCTYPE html>
<html lang="en">
<head>
<meta charset="utf-8">
<title>VMGD — Craft Cocktail Mixes</title>
<link href="https://fonts.googleapis.com/css2?family=Montserrat:wght@500;600;700;800;900&family=Open+Sans:wght@400;600&display=swap" rel="stylesheet">
<style>
:root{
  --teal:#00AB8E;
  --teal-mid:#00BBA5;
  --teal-soft:#67D7C9;
  --teal-pale:#C6EFE9;
  --teal-mist:#E9F9F6;
  --ink:#222222;
  --dark:#232323;
  --text:#333333;
  --line:#d9d9d9;
  --white:#ffffff;
}
*{box-sizing:border-box;margin:0;padding:0}
html,body{width:1200px;height:3984px;overflow:hidden;background:var(--white)}
body{position:relative;font-family:"Open Sans",Arial,sans-serif;color:var(--text)}
.abs{position:absolute}
.heading{font-family:"Montserrat",Arial,sans-serif;font-weight:800;color:var(--ink)}
.btn{position:absolute;display:flex;align-items:center;justify-content:center;background:var(--teal);color:var(--white);font-family:"Montserrat",Arial,sans-serif;font-weight:700;text-transform:uppercase}

/* header */
.site-header{left:0;top:0;width:1200px;height:108px;background:var(--teal)}
.brand{left:130px;top:22px;display:flex;align-items:center;gap:10px;font-family:"Montserrat",Arial,sans-serif;font-weight:800;font-size:40px;color:var(--white);letter-spacing:2px}
.brand-dot{width:18px;height:18px;border-radius:50%;background:var(--white)}
.brand-tag{left:134px;top:76px;font-family:"Montserrat",Arial,sans-serif;font-weight:800;font-size:9px;letter-spacing:2px;color:var(--white);text-transform:uppercase}
.follow{left:744px;top:27px;font-size:11px;color:var(--white);display:flex;align-items:center;gap:6px}
.social-dot{width:23px;height:23px;border-radius:50%;background:var(--teal-pale)}
.icon-search{left:930px;top:27px}
.icon-cart{left:980px;top:24px}
.cart-badge{left:998px;top:20px;width:15px;height:15px;border-radius:50%;background:var(--teal-pale);color:var(--ink);font-size:9px;display:flex;align-items:center;justify-content:center}
.cart-label{left:1018px;top:33px;font-size:11px;color:var(--white)}
.main-nav{left:556px;top:72px;display:flex;gap:46px;font-size:15px;color:var(--white)}
.main-nav .active{border-bottom:1.5px solid var(--white);padding-bottom:3px}

/* hero */
.hero{left:0;top:108px;width:1200px;height:557px;background:linear-gradient(180deg,#7cc8c8 0%,#a6d9d8 60%,#c9d9cf 78%,#dfe6de 100%)}
.hero-art{left:30px;top:140px;width:530px;height:500px;border-radius:40px;background:radial-gradient(ellipse at 50% 55%,#e3b27a 0%,#b9c98e 45%,rgba(160,200,170,0) 75%)}
.hero-title{left:660px;top:205px;font-size:65px;line-height:66px;font-weight:900;color:#2a2a2a}
.hero-btn{left:667px;top:430px;width:160px;height:57px;background:var(--white);color:var(--ink);font-size:18px;display:flex;align-items:center;justify-content:center;border-radius:3px}
.dots{left:563px;top:626px;display:flex;gap:9px}
.dots span{width:7px;height:7px;border-radius:50%;background:#333}
.dots .on{background:var(--teal)}

/* section titles */
.section-title{width:1200px;left:0;text-align:center;font-size:26px}
.title-rule{left:575px;width:50px;height:2px;background:var(--teal-soft)}

/* product cards */
.card{width:301px;height:395px;border:1px solid var(--line);background:var(--white)}
.card .photo{position:absolute;left:0;top:0;width:100%;height:235px}
.card .name{position:absolute;left:0;top:262px;width:100%;text-align:center;font-family:"Montserrat",Arial,sans-serif;font-weight:700;font-size:16px;color:var(--ink)}
.card .price{position:absolute;left:0;top:292px;width:100%;text-align:center;font-size:20px;color:var(--ink)}
.card .btn{left:98px;top:330px;width:104px;height:28px;font-size:11px}
.arrow{width:20px;height:30px}

/* feature band */
.feature{left:0;top:1250px;width:1200px;height:485px;background:var(--dark)}
.feature-photo{left:577px;top:1250px;width:623px;height:485px;background:radial-gradient(circle at 55% 45%,#c98b52 0%,#8a5a3a 35%,#3b3a38 75%,#2b2d2f 100%)}
.feature-title{left:131px;top:1333px;width:330px;font-size:27px;line-height:31px;color:var(--white)}
.body-copy{width:330px;font-size:16px;line-height:22.5px}
.feature-copy{left:131px;top:1453px;color:#e4e4e4}

/* choose band */
.choose-bg{left:0;top:2325px;width:1200px;height:460px;background:var(--teal-mist)}
.choose-title{left:131px;top:2417px;font-size:27px}
.choose-copy{left:131px;top:2478px;color:var(--text)}
.drink{width:100px;height:150px;border-radius:14px}

/* blog */
.post{width:304px;height:400px;background:var(--white);box-shadow:0 1px 6px rgba(0,0,0,.12)}
.post .photo{position:absolute;left:0;top:0;width:100%;height:192px}
.post h3{position:absolute;left:28px;top:222px;width:260px;font-family:"Montserrat",Arial,sans-serif;font-weight:800;font-size:12px;line-height:18px;color:var(--ink);text-transform:uppercase}
.post p{position:absolute;left:28px;top:268px;width:260px;font-size:13px;line-height:19px;color:var(--text)}
.post .btn{left:30px;top:345px;width:88px;height:30px;font-size:9px}

/* newsletter */
.newsletter{left:0;top:3387px;width:1200px;height:248px;background:var(--teal)}
.news-title{left:0;top:3435px;width:1200px;text-align:center;font-size:24px;color:var(--white)}
.news-copy{left:0;top:3474px;width:1200px;text-align:center;font-size:16px;color:var(--teal-mist)}
.email{left:327px;top:3522px;width:395px;height:53px;background:var(--white);font-size:15px;color:var(--ink);padding:16px 20px}
.subscribe{left:722px;top:3522px;width:151px;height:53px;background:#111;color:var(--white);font-family:"Montserrat",Arial,sans-serif;font-weight:800;font-size:15px;display:flex;align-items:center;justify-content:center}

/* footer */
.site-footer{left:0;top:3635px;width:1200px;height:349px;background:var(--dark)}
.foot-brand{left:131px;top:3712px;display:flex;align-items:center;gap:14px;font-family:"Montserrat",Arial,sans-serif;font-weight:800;font-size:64px;color:var(--white);letter-spacing:3px}
.foot-brand .dot{width:26px;height:26px;border-radius:50%;background:var(--white)}
.foot-tag{left:136px;top:3800px;font-family:"Montserrat",Arial,sans-serif;font-weight:800;font-size:13px;letter-spacing:3px;color:var(--white);text-transform:uppercase}
.foot-head{font-family:"Montserrat",Arial,sans-serif;font-weight:800;font-size:12px;color:var(--white);top:3680px}
.foot-list{font-size:11.5px;line-height:20px;color:#e6e6e6;list-style:none}
.contact-row{display:flex;gap:12px;align-items:flex-start;font-size:11.5px;line-height:15px;color:#e6e6e6}
.circle-ico{width:24px;height:24px;border-radius:50%;background:var(--white);flex:none;display:flex;align-items:center;justify-content:center}
.foot-rule{left:131px;top:3878px;width:938px;height:1px;background:#3d3d3d}
.copyright{left:0;top:3940px;width:1200px;text-align:center;font-size:10px;color:#d0d0d0}
</style>
</head>
<body>

<header class="abs site-header">
  <div class="abs brand"><span>VMGD</span><span class="brand-dot"></span></div>
  <div class="abs brand-tag">Velvet Marrow Glee Den</div>
  <div class="abs follow">FOLLOW US <span class="social-dot"></span><span class="social-dot"></span><span class="social-dot"></span></div>
  <svg class="abs icon-search" width="22" height="22" viewBox="0 0 22 22"><circle cx="9" cy="9" r="6.5" fill="none" stroke="#fff" stroke-width="3"/><line x1="14" y1="14" x2="20" y2="20" stroke="#fff" stroke-width="3.5" stroke-linecap="round"/></svg>
  <svg class="abs icon-cart" width="26" height="24" viewBox="0 0 26 24"><path d="M1 2h4l3 13h13l3-9H7" fill="none" stroke="#fff" stroke-width="2.5"/><path d="M7 6h17l-3 9H9z" fill="#fff"/><circle cx="10" cy="20" r="2.2" fill="#fff"/><circle cx="19" cy="20" r="2.2" fill="#fff"/></svg>
  <div class="abs cart-badge">0</div>
  <div class="abs cart-label">MY CART</div>
  <nav class="abs main-nav"><span class="active">HOME</span><span>ABOUT US</span><span>PRODUCTS</span><span>BLOG</span><span>CONTACT US</span></nav>
</header>

<section class="abs hero" aria-label="Hero"></section>
<div class="abs hero-art" role="img" aria-label="Mason jar of cucumber and citrus infusion beside a lime and grapefruit slices"></div>
<h1 class="abs heading hero-title">CRAFT<br>COCKTAIL<br>MIXES</h1>
<div class="abs hero-btn">READ MORE</div>
<div class="abs dots"><span></span><span></span><span class="on"></span><span></span><span></span></div>

<h2 class="abs heading section-title" style="top:715px">OUR PRODUCTS</h2>
<div class="abs title-rule" style="top:768px"></div>
<svg class="abs arrow" style="left:70px;top:962px" viewBox="0 0 20 30"><path d="M14 5L5 15l9 10" fill="none" stroke="#111" stroke-width="3"/></svg>
<svg class="abs arrow" style="left:1100px;top:962px" viewBox="0 0 20 30"><path d="M6 5l9 10-9 10" fill="none" stroke="#111" stroke-width="3"/></svg>

<article class="abs card" style="left:131px;top:800px"><div class="photo" role="img" aria-label="Jar of dried orange slices" style="background:radial-gradient(circle at 50% 55%,#eea66a 0%,#f3d3b2 45%,#f1f1ec 80%)"></div><div class="name">LOREM IPSUM</div><div class="price">$5.55</div><div class="btn">Add to cart</div></article>
<article class="abs card" style="left:450px;top:800px"><div class="photo" role="img" aria-label="Clip-top jar of dried fruit pieces" style="background:radial-gradient(ellipse at 50% 50%,#d9b487 0%,#ece1d3 30%,#fff 55%)"></div><div class="name">LOREM IPSUM</div><div class="price">$5.55</div><div class="btn">Add to cart</div></article>
<article class="abs card" style="left:769px;top:800px"><div class="photo" role="img" aria-label="Open jar of dried mushrooms and herbs" style="background:radial-gradient(ellipse at 50% 50%,#6f6a52 0%,#bfbda8 30%,#fff 58%)"></div><div class="name">LOREM IPSUM</div><div class="price">$5.55</div><div class="btn">Add to cart</div></article>

<section class="abs feature" aria-label="Feature"></section>
<div class="abs feature-photo" role="img" aria-label="Close-up of dried orange slices in a glass"></div>
<h2 class="abs heading feature-title">Lorem Ipsum is simply dummy text of the printing</h2>
<p class="abs body-copy feature-copy">There are many variations of passages of Lorem Ipsum available, but the majority have suffered alteration in some form, by injected humour, or randomised words which don't look even slightly believable.</p>
<div class="btn" style="left:131px;top:1594px;width:113px;height:38px;font-size:12px">Read more</div>

<h2 class="abs heading section-title" style="top:1782px">NEW PRODUCTS</h2>
<div class="abs title-rule" style="top:1828px"></div>
<svg class="abs arrow" style="left:66px;top:2043px" viewBox="0 0 20 30"><path d="M14 5L5 15l9 10" fill="none" stroke="#111" stroke-width="3"/></svg>
<svg class="abs arrow" style="left:1103px;top:2043px" viewBox="0 0 20 30"><path d="M6 5l9 10-9 10" fill="none" stroke="#111" stroke-width="3"/></svg>

<article class="abs card" style="left:131px;top:1867px"><div class="photo" role="img" aria-label="Clip-top jar of dried citrus" style="background:radial-gradient(ellipse at 50% 55%,#d9a76d 0%,#eedbc4 30%,#fff 55%)"></div><div class="name">LOREM IPSUM</div><div class="price">$5.55</div><div class="btn">Add to cart</div></article>
<article class="abs card" style="left:450px;top:1867px"><div class="photo" role="img" aria-label="Clip-top jar of dark dried ingredients" style="background:radial-gradient(ellipse at 50% 55%,#3d3f38 0%,#a7a89f 33%,#fff 58%)"></div><div class="name">LOREM IPSUM</div><div class="price">$5.55</div><div class="btn">Add to cart</div></article>
<article class="abs card" style="left:769px;top:1867px"><div class="photo" role="img" aria-label="Glass jar of dried green herbs" style="background:radial-gradient(ellipse at 50% 55%,#55604a 0%,#b4b9aa 30%,#fff 55%)"></div><div class="name">LOREM IPSUM</div><div class="price">$5.55</div><div class="btn">Add to cart</div></article>

<section class="abs choose-bg" aria-label="Choose your cocktail"></section>
<h2 class="abs heading choose-title">Choose your Cocktail</h2>
<p class="abs body-copy choose-copy">There are many variations of passages of Lorem Ipsum available, but the majority have suffered alteration in some form, by injected humour, or randomised words which don't look even slightly believable.</p>
<div class="btn" style="left:131px;top:2618px;width:113px;height:38px;font-size:12px">Read more</div>
<div class="abs drink" style="left:512px;top:2372px;background:linear-gradient(180deg,#e9f9f6,#8fd19a)" role="img" aria-label="Illustrated green mojito glass"></div>
<div class="abs drink" style="left:663px;top:2372px;background:linear-gradient(180deg,#e9f9f6,#e95f86)" role="img" aria-label="Illustrated pink cocktail"></div>
<div class="abs drink" style="left:813px;top:2372px;background:linear-gradient(180deg,#e9f9f6,#f4c64a 50%,#e9f9f6)" role="img" aria-label="Illustrated yellow martini"></div>
<div class="abs drink" style="left:963px;top:2372px;background:linear-gradient(180deg,#e9f9f6,#f7c94b)" role="img" aria-label="Illustrated lemon drink"></div>
<div class="abs drink" style="left:512px;top:2568px;height:160px;background:linear-gradient(180deg,#e9f9f6,#d8e58f)" role="img" aria-label="Illustrated lime highball"></div>
<div class="abs drink" style="left:663px;top:2568px;height:160px;background:linear-gradient(180deg,#e9f9f6,#a9d7cf)" role="img" aria-label="Illustrated mint water glass"></div>
<div class="abs drink" style="left:813px;top:2568px;height:160px;background:linear-gradient(180deg,#e9f9f6,#e84f7b)" role="img" aria-label="Illustrated berry cocktail with orange"></div>
<div class="abs drink" style="left:963px;top:2600px;height:125px;background:linear-gradient(180deg,#e9f9f6,#f08a3a)" role="img" aria-label="Illustrated orange tumbler"></div>

<h2 class="abs heading section-title" style="top:2832px">LATEST BLOG</h2>
<div class="abs title-rule" style="top:2884px"></div>

<article class="abs post" style="left:131px;top:2925px"><div class="photo" role="img" aria-label="Grapefruit slices in a glass with herbs" style="background:linear-gradient(135deg,#4a5a2e,#d9603a 55%,#c8a06b)"></div><h3>Contrary to popular belief Lorem Ipsum is not simpl</h3><p>There are many variations of passages of Lorem Ipsum ava ilable, but the majority have suffered alteration.</p><div class="btn">Read more</div></article>
<article class="abs post" style="left:449px;top:2925px"><div class="photo" role="img" aria-label="Jars of dried citrus on a shelf" style="background:linear-gradient(180deg,#dfe3e8,#c9ced4 55%,#7a5b40)"></div><h3>Contrary to popular belief Lorem Ipsum is not simpl</h3><p>There are many variations of passages of Lorem Ipsum ava ilable, but the majority have suffered alteration.</p><div class="btn">Read more</div></article>
<article class="abs post" style="left:765px;top:2925px"><div class="photo" role="img" aria-label="Iced amber cocktails with limes" style="background:linear-gradient(135deg,#6a7d3a,#c47a2a 50%,#3a2518)"></div><h3>Contrary to popular belief Lorem Ipsum is not simpl</h3><p>There are many variations of passages of Lorem Ipsum ava ilable, but the majority have suffered alteration.</p><div class="btn">Read more</div></article>

<section class="abs newsletter" aria-label="Newsletter"></section>
<h2 class="abs heading news-title">SUBSCRIBE NEWSLETTER</h2>
<p class="abs news-copy">There are many variations of passages of Lorem Ipsum ava ilable</p>
<div class="abs email">Email id</div>
<div class="abs subscribe">SUBSCRIBE</div>

<footer class="abs site-footer"></footer>
<div class="abs foot-brand"><span>VMGD</span><span class="dot"></span></div>
<div class="abs foot-tag">Velvet Marrow Glee Den</div>

<div class="abs foot-head" style="left:480px">MENU</div>
<ul class="abs foot-list" style="left:480px;top:3712px"><li>HOME</li><li>ABOUT US</li><li>PRODUCTS</li><li>BLOG</li><li>CONTACT US</li></ul>

<div class="abs foot-head" style="left:670px">CONTACT US</div>
<div class="abs contact-row" style="left:668px;top:3714px"><span class="circle-ico"><svg width="10" height="13" viewBox="0 0 10 13"><path d="M5 0a5 5 0 0 1 5 5c0 4-5 8-5 8S0 9 0 5a5 5 0 0 1 5-5z" fill="#222"/><circle cx="5" cy="5" r="1.8" fill="#fff"/></svg></span><span>5127 Larkspur Row<br>Calverton, OR 97342</span></div>
<div class="abs contact-row" style="left:668px;top:3773px"><span class="circle-ico"><svg width="12" height="12" viewBox="0 0 12 12"><path d="M2 0l3 3-1.5 1.5a7 7 0 0 0 4 4L9 7l3 3-2 2C5 12 0 7 0 2z" fill="#222"/></svg></span><span>Call Us<br>555.014.2290</span></div>
<div class="abs contact-row" style="left:668px;top:3825px"><span class="circle-ico"><svg width="12" height="9" viewBox="0 0 12 9"><rect width="12" height="9" fill="#222"/><path d="M0 0l6 5 6-5" fill="none" stroke="#fff" stroke-width="1"/></svg></span><span>E mail Us<br>info@VMGD.com</span></div>

<div class="abs foot-head" style="left:962px">FOLLOW US</div>
<div class="abs contact-row" style="left:960px;top:3714px"><span class="circle-ico"></span><span>Like us on<br>FRIENDWALL</span></div>
<div class="abs contact-row" style="left:960px;top:3773px"><span class="circle-ico"></span><span>Follow us on<br>CHIRPLINE</span></div>
<div class="abs contact-row" style="left:960px;top:3825px"><span class="circle-ico"></span><span>Follow us on<br>WORKWEAVE</span></div>

<div class="abs foot-rule"></div>
<div class="abs copyright">Copyright © 2021 All Rights Reserved</div>

</body>
</html>
```